wealth management firm, professional group, new model

we have a logo that works but we need a card, white background using our colors...clean look

our tag line if can be used in

Steady Growth For Every Family

```html
<!DOCTYPE html>
<html lang="it">
<head>
<meta charset="utf-8">
<title>Arvena Wealth Partners – Biglietto da visita</title>
<link href="https://fonts.googleapis.com/css2?family=Montserrat:wght@400;500;700&display=swap" rel="stylesheet">
<style>
  :root {
    --navy: #14295a;
    --navy-deep: #0d1c40;
    --navy-light: #24407e;
    --ink: #1a2d5c;
    --text: #3a3f4d;
    --white: #ffffff;
    --stage: #e6e7ea;
  }
  * { box-sizing: border-box; margin: 0; padding: 0; }
  html, body {
    width: 1200px; height: 980px; overflow: hidden;
    background: var(--stage);
    font-family: "Montserrat", sans-serif;
  }
  .stage { position: relative; width: 1200px; height: 980px; }
  .card {
    position: absolute; left: 330px;
    width: 540px; height: 308px;
    box-shadow: 0 14px 32px rgba(20, 30, 60, 0.18);
    overflow: hidden;
  }
  /* Front */
  .card--front { top: 110px; color: var(--white); }
  .card__pattern {
    position: absolute; inset: 0;
    background: linear-gradient(135deg, var(--navy-light) 0%, var(--navy) 45%, var(--navy-deep) 100%);
  }
  .front__content {
    position: relative; height: 100%;
    display: flex; flex-direction: column; align-items: center; justify-content: center;
    text-align: center;
  }
  .brand-name {
    font-weight: 400; font-size: 50px; letter-spacing: 0.42em;
    margin-right: -0.42em; line-height: 1; white-space: nowrap;
  }
  .brand-sub {
    font-weight: 400; font-size: 17px; letter-spacing: 0.2em;
    margin-top: 16px; margin-right: -0.2em; white-space: nowrap;
  }
  .tagline {
    font-weight: 400; font-size: 12px; letter-spacing: 0.2em;
    text-transform: uppercase; margin-top: 14px; margin-right: -0.2em;
  }
  /* Back */
  .card--back {
    top: 540px; background: var(--white);
    display: flex; align-items: center;
  }
  .back__brand {
    width: 272px; display: flex; flex-direction: column; align-items: center;
    color: var(--ink); padding: 0 24px;
  }
  .back__brand .brand-name { font-size: 32px; letter-spacing: 0.36em; margin-right: -0.36em; }
  .back__brand .brand-sub { font-size: 12px; margin-top: 14px; }
  .divider { width: 1px; height: 170px; background: var(--ink); flex: none; }
  .contact {
    padding-left: 24px; color: var(--text);
    font-size: 13px; line-height: 1.35;
  }
  .contact__name {
    font-weight: 700; font-size: 17px; color: var(--ink); text-transform: uppercase;
  }
  .contact__role { margin-bottom: 12px; }
  .contact__row { display: flex; align-items: flex-start; gap: 10px; margin-bottom: 2px; }
  .contact__row--gap { margin-bottom: 12px; }
  .contact__row svg {
    width: 14px; height: 14px; flex: none; margin-top: 2px;
    stroke: var(--ink); fill: none; stroke-width: 1.5;
  }
</style>
</head>
<body>
<main class="stage">

  <section class="card card--front">
    <div class="card__pattern" role="img" aria-label="Motivo poligonale a sfaccettature in toni di blu navy"></div>
    <div class="front__content">
      <div class="brand-name">ARVENA</div>
      <div class="brand-sub">WEALTH PARTNERS</div>
      <div class="tagline">Steady Growth For Every Family</div>
    </div>
  </section>

  <section class="card card--back">
    <div class="back__brand">
      <div class="brand-name">ARVENA</div>
      <div class="brand-sub">WEALTH PARTNERS</div>
    </div>
    <div class="divider"></div>
    <div class="contact">
      <div class="contact__name">Marco Ferrante</div>
      <div class="contact__role">CEO e Fondatore</div>
      <div class="contact__row contact__row--gap">
        <svg viewBox="0 0 16 16"><path d="M8 15s5-5 5-8.5a5 5 0 0 0-10 0C3 10 8 15 8 15z"/><circle cx="8" cy="6.5" r="1.8"/></svg>
        <span>Via Solari 14<br>20144 Milano</span>
      </div>
      <div class="contact__row">
        <svg viewBox="0 0 16 16"><path d="M3 2h3l1.2 3-1.7 1.2a8 8 0 0 0 4.3 4.3L11 8.8l3 1.2v3a1 1 0 0 1-1 1A12 12 0 0 1 2 3a1 1 0 0 1 1-1z"/></svg>
        <span>+39.340.555.0182</span>
      </div>
      <div class="contact__row">
        <svg viewBox="0 0 16 16"><rect x="1.5" y="3.5" width="13" height="9"/><path d="M1.5 3.5 8 9l6.5-5.5"/></svg>
        <span>info@arvenamail.com</span>
      </div>
      <div class="contact__row">
        <svg viewBox="0 0 16 16"><circle cx="8" cy="8" r="6.5"/><ellipse cx="8" cy="8" rx="2.8" ry="6.5"/><path d="M1.5 8h13"/></svg>
        <span>www.arvenaweb.com</span>
      </div>
    </div>
  </section>

</main>
</body>
</html>
```